Business Cards

I'd like help creating business cards with the full logo "Veltrona Capital Partners" on the back of the card (navy background with white writing), and abbreviated logo "Veltrona" on the front. Would like to list name, title, phone number, email, and website listed on front of card. Would like to keep very simple. Front font Arial or similar.

```html
<!DOCTYPE html>
<html lang="en">
<head>
<meta charset="utf-8">
<title>Veltrona Capital Partners – Business Cards</title>
<link href="https://fonts.googleapis.com/css2?family=Montserrat:wght@500;700&display=swap" rel="stylesheet">
<style>
  :root {
    --navy: #3a4456;
    --white: #ffffff;
    --orange-light: #f89b3e;
    --orange-deep: #f27545;
    --brand-font: "Montserrat", Arial, sans-serif;
    --name-font: Arial, "Helvetica Neue", sans-serif;
  }
  html, body {
    margin: 0;
    padding: 0;
    width: 994px;
    height: 1200px;
    overflow: hidden;
    background: var(--white);
  }
  .sheet {
    position: relative;
    width: 994px;
    height: 1200px;
  }
  .card {
    position: absolute;
    left: 0;
    width: 994px;
    background: var(--navy);
    overflow: hidden;
  }
  .card--back { top: 0; height: 583px; }
  .card--front { top: 617px; height: 583px; }

  .company-name {
    position: absolute;
    left: 0;
    right: 0;
    top: 262px;
    margin: 0;
    text-align: center;
    color: var(--white);
    font-family: var(--brand-font);
    font-weight: 700;
    font-size: 46px;
    line-height: 1;
    letter-spacing: 0;
  }

  .front-mark {
    position: absolute;
    right: 48px;
    top: 78px;
    display: flex;
    align-items: center;
    gap: 12px;
    color: var(--white);
    font-family: var(--brand-font);
    font-weight: 700;
    font-size: 36px;
    line-height: 1;
  }
  .front-mark__square {
    width: 18px;
    height: 18px;
    background: var(--white);
  }

  .contact-list {
    position: absolute;
    left: 0;
    top: 176px;
    margin: 0;
    padding: 0;
    list-style: none;
  }
  .contact-item {
    display: flex;
    align-items: center;
    height: 53px;
    margin-bottom: 18px;
  }
  .contact-item__tab {
    position: relative;
    width: 169px;
    height: 53px;
    border-radius: 0 27px 27px 0;
    background: linear-gradient(90deg, var(--orange-light), var(--orange-deep));
    flex: none;
  }
  .contact-item__tab svg {
    position: absolute;
    left: 120px;
    top: 15px;
    width: 23px;
    height: 23px;
  }
  .contact-item__text {
    margin-left: 9px;
    color: var(--white);
    font-family: var(--brand-font);
    font-weight: 500;
    font-size: 20px;
    letter-spacing: 1px;
    white-space: nowrap;
  }

  .holder-name {
    position: absolute;
    right: 58px;
    top: 291px;
    margin: 0;
    color: var(--white);
    font-family: var(--name-font);
    font-weight: 400;
    font-size: 49px;
    line-height: 1;
    letter-spacing: 0.5px;
  }

  .accent-peak {
    position: absolute;
    left: 669px;
    top: 437px;
    width: 274px;
    height: 146px;
  }
</style>
</head>
<body>
<main class="sheet">

  <section class="card card--back" aria-label="Card back">
    <p class="company-name">Veltrona Capital Partners</p>
  </section>

  <section class="card card--front" aria-label="Card front">
    <div class="front-mark">
      <span class="front-mark__square" aria-hidden="true"></span>
      <span>Veltrona</span>
    </div>

    <ul class="contact-list">
      <li class="contact-item">
        <span class="contact-item__tab">
          <svg viewBox="0 0 24 24" aria-hidden="true"><path fill="#fff" fill-rule="evenodd" d="M12 1a8 8 0 0 0-8 8c0 3 2 5.5 8 14 6-8.5 8-11 8-14a8 8 0 0 0-8-8zm0 5a3 3 0 1 1 0 6 3 3 0 0 1 0-6z"/></svg>
        </span>
        <span class="contact-item__text">STREET NAME, STATE, COUNTRY</span>
      </li>
      <li class="contact-item">
        <span class="contact-item__tab">
          <svg viewBox="0 0 24 24" aria-hidden="true"><path fill="#fff" d="M1 5h22v1.5l-11 7-11-7zM1 9l11 7 11-7v10H1z"/></svg>
        </span>
        <span class="contact-item__text">HELLO@VELTRONAMAIL.COM</span>
      </li>
      <li class="contact-item">
        <span class="contact-item__tab">
          <svg viewBox="0 0 24 24" aria-hidden="true"><path fill="#fff" d="M4 1c1.5-.5 2.5 1 3 2.5l1 3c.3 1-.5 1.8-1.2 2.5 1.5 3.5 4 6 7.3 7.4.8-.7 1.6-1.4 2.6-1l3 1.3c1.5.6 2.5 2 1.8 3-1 1.5-3 2.5-5.5 2C9 20.5 3.5 15 2 9 1.3 5.5 2.5 2 4 1z"/></svg>
        </span>
        <span class="contact-item__text">555 2840 31700</span>
      </li>
      <li class="contact-item">
        <span class="contact-item__tab">
          <svg viewBox="0 0 24 24" aria-hidden="true"><g fill="none" stroke="#fff" stroke-width="1.4"><circle cx="12" cy="12" r="10.5"/><ellipse cx="12" cy="12" rx="4.5" ry="10.5"/><path d="M12 1.5v21M1.5 12h21M3 7h18M3 17h18"/></g></svg>
        </span>
        <span class="contact-item__text">WWW.VELTRONACAPITAL.COM</span>
      </li>
    </ul>

    <h1 class="holder-name">YOUR NAME</h1>

    <svg class="accent-peak" viewBox="0 0 274 146" aria-hidden="true">
      <defs>
        <linearGradient id="peakGradient" x1="0" y1="0" x2="1" y2="0">
          <stop offset="0" stop-color="#f89b3e"/>
          <stop offset="1" stop-color="#f27545"/>
        </linearGradient>
      </defs>
      <path fill="url(#peakGradient)" d="M0 130 L121 9 Q137 -5 153 9 L274 130 L274 146 L0 146 Z"/>
    </svg>
  </section>

</main>
</body>
</html>
```